IT Company needs a Wordpress Web Design

We need a wordpress website for a new IT Company called 'RJ Systemworks'. We develop educational software for Middle and High School Students and Staff. Our initial product is DeskRoute - a web app that allows School Counselors to track information about the students that they see. We would like to see modern designs that include the company logo and the DeskRoute logo

Target Market(s)

Educators

Industry/Entity Type

Information Technology

Coding

Coded - Design and coding required

Number of Pages Required

1 page

Font styles to use
Sans Serif

Requirements
Must have
• Must be able to use WordPress
Should not have
• No Flash

```html
<!DOCTYPE html>
<html lang="en">
<head>
<meta charset="utf-8">
<title>RJ Systemworks – DeskRoute</title>
<link href="https://fonts.googleapis.com/css2?family=Montserrat:wght@400;500;600;700&family=Arimo:wght@400;700&display=swap" rel="stylesheet">
<style>
:root{
  --blue:#4a86c5;
  --blue-light:#8fb4dc;
  --blue-pale:#a9c7e6;
  --dark:#262626;
  --btn:#2b2b2b;
  --grey:#e4e4e4;
  --red:#c4262e;
  --white:#ffffff;
  --text:#4a4a4a;
}
*{margin:0;padding:0;box-sizing:border-box}
html,body{width:687px;height:1200px;overflow:hidden}
body{position:relative;font-family:"Arimo",Arial,sans-serif;background:var(--white);color:var(--text)}
.abs{position:absolute}
.heading{font-family:"Montserrat",Arial,sans-serif}

/* hero */
.hero{left:0;top:0;width:687px;height:388px;background:linear-gradient(120deg,#6f99c6 0%,#87aed8 45%,#a6c4e4 100%)}
.brand{left:44px;top:8px;width:64px;height:40px;border:2px solid var(--white);display:flex;align-items:center;justify-content:center;text-align:center;color:var(--white);font-family:"Montserrat",sans-serif;font-weight:700;font-size:9px;line-height:10px}
.nav{right:44px;top:20px;display:flex;gap:33px;align-items:center}
.nav a{color:var(--white);font-family:"Montserrat",sans-serif;font-weight:500;font-size:10px;text-decoration:none;letter-spacing:.3px;position:relative}
.nav a.active::before{content:"";position:absolute;left:50%;top:-20px;width:1px;height:14px;background:var(--white)}
.nav a.active::after{content:"";position:absolute;left:calc(50% - 2.5px);top:-7px;width:5px;height:5px;border:1px solid var(--white);border-radius:50%}
.hero-copy{left:46px;top:128px;color:var(--white)}
.hero-copy .kicker{font-size:16px;font-weight:600}
.hero-copy h1{font-size:37px;font-weight:600;letter-spacing:1px;line-height:42px}
.hero-copy .sub{font-size:18px;font-weight:500;line-height:24px;margin-top:8px}
.hero-copy .sub b{font-weight:700}
.btn{display:flex;align-items:center;justify-content:center;background:var(--btn);color:var(--white);border-radius:16px;font-size:10.5px;text-decoration:none}
.hero .btn{left:44px;top:261px;width:114px;height:30px}

/* features */
.features{left:0;top:388px;width:687px;height:166px;background:var(--dark)}
.feature{top:0;width:150px;text-align:center;color:var(--white)}
.feature svg{display:block;margin:30px auto 0;height:38px}
.feature h3{font-family:"Montserrat",sans-serif;font-size:9.6px;font-weight:600;letter-spacing:.3px;margin-top:14px}
.feature p{font-size:7.8px;line-height:13px;margin-top:6px}
.features .underline{left:44px;top:164px;width:143px;height:2px;background:var(--blue)}

/* pricing */
.pricing-title{left:0;top:582px;width:687px;text-align:center;font-size:23px;font-weight:500;letter-spacing:.5px}
.pricing-title .product{color:var(--red);font-weight:700}
.pricing-title .word{color:var(--blue)}
.plan{top:627px;width:286px;height:202px;border-radius:4px;background:linear-gradient(135deg,#7ea6d1 0%,#9bbde2 55%,#6d97c6 100%);color:var(--white);overflow:hidden}
.plan h2{position:absolute;left:19px;top:17px;font-size:14.5px;font-weight:500;line-height:17.5px;letter-spacing:.4px}
.plan .price{position:absolute;left:19px;top:58px;font-size:24px;font-weight:600}
.plan .unit{position:absolute;left:19px;top:90px;font-size:7.5px}
.plan .btn{position:absolute;left:155px;top:155px;width:113px;height:29px}

/* promo */
.promo{left:0;top:860px;width:687px;height:166px;background:var(--grey);text-align:center}
.promo-brand{display:flex;justify-content:center;align-items:center;gap:8px;margin-top:30px}
.promo-brand .mark{width:22px;height:22px;background:var(--red)}
.promo-brand .name{font-family:"Montserrat",sans-serif;font-weight:700;font-size:20px;color:var(--red)}
.promo .tagline{font-size:7.5px;color:var(--dark);margin-top:1px;margin-left:30px}
.promo p{font-size:9.6px;line-height:13px;color:var(--text);margin:4px auto 0;width:400px}
.promo .btn{position:absolute;left:287px;top:106px;width:113px;height:31px;background:var(--blue)}

/* footer */
.footer{left:0;top:1026px;width:687px;height:138px;background:var(--dark);color:var(--white)}
.footer h4{font-family:"Montserrat",sans-serif;font-size:10.5px;font-weight:500;letter-spacing:.4px;display:flex;align-items:center;gap:2px}
.footer h4::after{content:"";width:6px;height:6px;border:1px solid var(--white);border-radius:50%;flex:none}
.footer h4 .rule{order:2;height:1px;background:var(--white);flex:1}
.col{top:19px}
.contact{left:46px;width:142px}
.contact li{list-style:none;display:flex;gap:9px;font-size:8.4px;line-height:15px;margin-top:8px}
.contact svg{flex:none;margin-top:3px}
.links{left:198px;width:142px}
.links ul{list-style:none;font-size:7.8px;line-height:15.6px;position:absolute;top:22px}
.links ul.first{left:0}
.links ul.second{left:72px}
.links li.current{font-weight:700}
.newsletter{left:350px;width:140px}
.newsletter p{font-size:7.8px;margin-top:12px}
.newsletter .field{margin-top:9px;width:143px;height:23px;border-radius:12px;background:#363636;color:#cfcfcf;font-size:7.8px;font-style:italic;display:flex;align-items:center;padding-left:12px}
.newsletter .btn{margin-top:3px;width:72px;height:23px;background:var(--blue);font-size:9.6px;font-weight:700;letter-spacing:.3px;border-radius:12px}
.footer-brand{left:538px;top:34px;width:62px;height:42px;border:2px solid var(--white);display:flex;align-items:center;justify-content:center;text-align:center;font-family:"Montserrat",sans-serif;font-weight:700;font-size:9px;line-height:10px}
.social{left:534px;top:88px;display:flex;gap:3px}
.social span{width:21px;height:21px;border:1.5px solid var(--white);border-radius:50%}
.bottom-bar{left:0;top:1164px;width:687px;height:36px;background:var(--blue);color:var(--white);font-size:8px;display:flex;align-items:center;justify-content:center;letter-spacing:.3px}
.bottom-bar b{color:var(--dark);font-weight:400}
</style>
</head>
<body>

<section class="abs hero">
  <div class="abs hero" role="img" aria-label="Photo of a relaxed man in glasses leaning back at his office desk with a laptop, tinted blue"></div>
  <div class="abs brand">RJ<br>SYSTEMWORKS</div>
  <nav class="abs nav">
    <a class="active" href="#">HOME</a>
    <a href="#">ABOUT</a>
    <a href="#">PRODUCTS</a>
    <a href="#">FAQ</a>
    <a href="#">CONTACT</a>
    <svg width="14" height="14" viewBox="0 0 14 14" aria-label="Search"><circle cx="5.8" cy="5.8" r="4.3" fill="none" stroke="#fff" stroke-width="2"/><line x1="9" y1="9" x2="13" y2="13" stroke="#fff" stroke-width="2.2" stroke-linecap="round"/></svg>
  </nav>
  <div class="abs hero-copy heading">
    <div class="kicker">FIND YOUR</div>
    <h1>COUNSELOR BUDDY</h1>
    <div class="sub">JOIN RJ SYSTEMWORKS FOR<br><b>DeskRoute</b> SOFTWARE</div>
  </div>
  <a class="abs btn" href="#">GET STARTED</a>
</section>

<section class="abs features">
  <div class="abs feature" style="left:41px">
    <svg viewBox="0 0 30 38" width="30"><rect x="1" y="1" width="28" height="36" fill="#1d3b5c" stroke="#4a86c5" stroke-width="1.5"/><line x1="5" y1="6" x2="25" y2="6" stroke="#4a86c5"/><line x1="5" y1="9" x2="20" y2="9" stroke="#4a86c5"/><g fill="#4a86c5"><rect x="6" y="24" width="2.5" height="6"/><rect x="10" y="20" width="2.5" height="10"/><rect x="14" y="22" width="2.5" height="8"/><rect x="18" y="17" width="2.5" height="13"/><rect x="22" y="23" width="2.5" height="7"/></g></svg>
    <h3>REPORTS AS ACCORDING</h3>
    <p>Generate Reports According to date, Grade Level, Visitor type, Conselor, Reson for Visit &amp; Many More.</p>
  </div>
  <div class="abs feature" style="left:193px">
    <svg viewBox="0 0 32 38" width="32"><path d="M8 17V10a8 8 0 0 1 16 0v7" fill="none" stroke="#fff" stroke-width="3.5"/><rect x="2" y="16" width="28" height="21" rx="2" fill="#fff"/><circle cx="16" cy="25" r="3" fill="#262626"/><rect x="15" y="26" width="2" height="6" fill="#262626"/></svg>
    <h3>CONFIDENTIAL SIGN-IN</h3>
    <p>Unlike a clipboard, guests sign in &amp; their information disappears from the screen. So no one know except you.</p>
  </div>
  <div class="abs feature" style="left:344px">
    <svg viewBox="0 0 48 38" width="48"><rect x="6" y="5" width="36" height="24" fill="none" stroke="#fff" stroke-width="2"/><path d="M1 31h46l-3 4H4z" fill="#fff"/><circle cx="13" cy="21" r="6" fill="#262626" stroke="#fff" stroke-width="1.5"/><circle cx="13" cy="19.5" r="2" fill="#fff"/><path d="M9.5 25a3.5 3.5 0 0 1 7 0" fill="#fff"/></svg>
    <h3>COLLECT DATA AUTOMATIC</h3>
    <p>Collecs your Individual Session data without lifting your finger. Just Sign in the one whom your are counselling.</p>
  </div>
  <div class="abs feature" style="left:495px">
    <svg viewBox="0 0 32 38" width="32"><rect x="2" y="4" width="24" height="32" fill="none" stroke="#fff" stroke-width="2"/><rect x="9" y="1" width="10" height="6" fill="#fff"/><g stroke="#fff" stroke-width="1.5"><line x1="6" y1="13" x2="22" y2="13"/><line x1="6" y1="18" x2="22" y2="18"/><line x1="6" y1="23" x2="17" y2="23"/></g><circle cx="24" cy="30" r="6.5" fill="#262626" stroke="#fff" stroke-width="1.5"/><path d="M21.5 27.5l5 5M26.5 27.5l-5 5" stroke="#fff" stroke-width="1.5"/></svg>
    <h3>GOOD BYE TO CLIPBOARD</h3>
    <p>DeskRoute is an electronic sign-in system that replaces your old-fashioned clipboard.</p>
  </div>
  <div class="abs underline"></div>
</section>

<h2 class="abs pricing-title heading"><span class="product">DeskRoute</span> <span class="word">PRICING</span></h2>

<article class="abs plan heading" style="left:44px">
  <div class="abs plan" style="left:0;top:0" role="img" aria-label="Photo of a smiling student at a laptop in a classroom, tinted blue"></div>
  <h2>INDIVIDUAL SCHOOL<br>PURCHASE</h2>
  <div class="price">$200</div>
  <div class="unit">PER SCHOOL</div>
  <a class="btn" href="#">GET STARTED</a>
</article>

<article class="abs plan heading" style="left:357px">
  <div class="abs plan" style="left:0;top:0;background:linear-gradient(135deg,#86acd5 0%,#a3c2e4 50%,#5f8dc0 100%)" role="img" aria-label="Photo of a group of smiling students, tinted blue"></div>
  <h2>DISTRICT LEVEL<br>PURCHASE</h2>
  <div class="price">$150</div>
  <div class="unit">PER SCHOOL</div>
  <a class="btn" href="#">GET STARTED</a>
</article>

<section class="abs promo">
  <div class="promo-brand"><span class="mark"></span><span class="name">DeskRoute</span></div>
  <div class="tagline">The Electronic Sign In System</div>
  <p>a web app that allows School Counselors to track information about the students that they see.</p>
  <a class="btn" href="#">GET STARTED</a>
</section>

<footer class="abs footer">
  <div class="abs col contact">
    <h4>CONTACT US <span class="rule"></span></h4>
    <ul>
      <li><svg width="9" height="11" viewBox="0 0 9 11"><path d="M4.5 0A4.5 4.5 0 0 0 0 4.5C0 7.5 4.5 11 4.5 11S9 7.5 9 4.5A4.5 4.5 0 0 0 4.5 0z" fill="#fff"/><circle cx="4.5" cy="4.5" r="1.6" fill="#262626"/></svg><span>123 Building Name, Street,<br>City, Country - Zip code</span></li>
      <li><svg width="9" height="9" viewBox="0 0 9 9"><path d="M1 0.5l2 0 1 2.3-1.2.9a5 5 0 0 0 2.5 2.5l.9-1.2 2.3 1v2C8.5 8.5 8 9 7.5 9 3.4 9 0 5.6 0 1.5 0 1 .5.5 1 .5z" fill="#fff"/></svg><span>01 2345 6789</span></li>
      <li><svg width="9" height="7" viewBox="0 0 9 7"><rect width="9" height="7" fill="#fff"/><path d="M0 0l4.5 3.8L9 0" fill="none" stroke="#262626"/></svg><span>info@rjsystemworks.com</span></li>
    </ul>
  </div>
  <div class="abs col links">
    <h4>QUICK LINKS <span class="rule"></span></h4>
    <ul class="first"><li class="current">• Home</li><li>• About</li><li>• Products</li><li>• Faq</li><li>• Contact</li></ul>
    <ul class="second"><li>• Privacy Policy</li><li>• Terms of Use</li><li>• Conditions</li></ul>
  </div>
  <div class="abs col newsletter">
    <h4>NEWSLETTER <span class="rule"></span></h4>
    <p>Get Latest News &amp; Updates About us.</p>
    <div class="field">E-Mail Address</div>
    <a class="btn" href="#">SUBSCRIBE</a>
  </div>
  <div class="abs footer-brand">RJ<br>SYSTEMWORKS</div>
  <div class="abs social"><span></span><span></span><span></span></div>
</footer>

<div class="abs bottom-bar heading">©&nbsp;<b>RJ SYSTEMWORKS</b>&nbsp;- 2017. All Rights Reserved.</div>

</body>
</html>
```